Stickers to put on my honeyglasses

Stickers for my honey glasses.
Only a single sticker on the front. Same should have a stripe on the top side which goes above the lid to show if the glass was opened.
Size of the main part should be 55mm high and max. 100 mm wide.
The stripe on the top should be 70mm long.
I added a Picture of another producer which uses the same glass as I do.
I should say: 'e Maringer Glas Hunneg'. which means 'another glass of honey. 'Hunneg' should be mainly visible and therefore very large. 'e Maringer Glas' should be less visible and therefore smaller above the 'Hunneg'
- It needs to contain the quantity : '500gr'
- It needs to contain my Name and address: 'Jos Maringer, 14, rue Pierre Faber, L-7590 Miersch' (This should be small and not to visible)
- It needs to conatin a validity Line: ´Am beschte virum:` (With enough space so I can add a date by hand)
- It needs to say: 'dréchen, kill andäischterstockéieren' (to store it dry cold and dark)

```html
<!DOCTYPE html>
<html lang="lb">
<head>
<meta charset="utf-8">
<title>Hunneg – Glas-Etikett</title>
<link rel="stylesheet" href="https://fonts.googleapis.com/css2?family=Playfair+Display:ital,wght@0,900;1,900&family=Questrial&display=swap">
<style>
  :root {
    --page: #ffffff;
    --paper: #f1ede2;
    --edge: #e39b0f;
    --gold-light: #fbd45a;
    --gold-mid: #f2b324;
    --gold-deep: #d98a06;
    --ink: #262421;
    --ink-soft: #3a3733;
    --meadow-green: #b8c98e;
    --meadow-pink: #e7b8bf;
    --meadow-violet: #b7a3cf;
    --bee-dark: #3b2f1f;
    --bee-yellow: #e9c24a;
  }
  html, body {
    margin: 0;
    padding: 0;
    width: 1200px;
    height: 1000px;
    overflow: hidden;
    background: var(--page);
  }
  .label-canvas {
    display: block;
    width: 1200px;
    height: 1000px;
  }
  .label-outline {
    fill: var(--paper);
    stroke: var(--edge);
    stroke-width: 4;
  }
  .tagline {
    font-family: "Playfair Display", Georgia, serif;
    font-style: italic;
    font-weight: 900;
    font-size: 29px;
    fill: var(--ink);
  }
  .product-name {
    font-family: "Playfair Display", Georgia, serif;
    font-weight: 900;
    font-size: 122px;
    letter-spacing: -1px;
  }
  .quantity {
    font-family: "Playfair Display", Georgia, serif;
    font-weight: 900;
    font-size: 25px;
    font-variant-numeric: lining-nums;
    fill: var(--ink);
  }
  .producer-address,
  .best-before,
  .storage-note {
    font-family: "Questrial", "Century Gothic", sans-serif;
    fill: var(--ink-soft);
  }
  .producer-address { font-size: 17px; }
  .best-before { font-size: 17px; }
  .storage-note { font-size: 19px; }
  .flight-trail {
    fill: none;
    stroke: var(--edge);
    stroke-width: 1.5;
    stroke-dasharray: 3 3;
  }
</style>
</head>
<body>
<svg class="label-canvas" viewBox="0 0 1200 1000" xmlns="http://www.w3.org/2000/svg">
  <defs>
    <linearGradient id="gold-ring" x1="0" y1="0" x2="1" y2="1">
      <stop offset="0" stop-color="var(--gold-light)"/>
      <stop offset="0.5" stop-color="var(--gold-deep)"/>
      <stop offset="1" stop-color="var(--gold-light)"/>
    </linearGradient>
    <linearGradient id="gold-letters" x1="0" y1="0" x2="0" y2="1">
      <stop offset="0" stop-color="var(--gold-deep)"/>
      <stop offset="0.45" stop-color="var(--gold-light)"/>
      <stop offset="1" stop-color="var(--gold-mid)"/>
    </linearGradient>
    <linearGradient id="meadow-tones" x1="0" y1="0" x2="0" y2="1">
      <stop offset="0" stop-color="var(--meadow-violet)" stop-opacity="0.55"/>
      <stop offset="0.35" stop-color="var(--meadow-pink)" stop-opacity="0.8"/>
      <stop offset="1" stop-color="var(--meadow-green)"/>
    </linearGradient>
    <radialGradient id="bee-tones" cx="0.5" cy="0.5" r="0.5">
      <stop offset="0" stop-color="var(--bee-yellow)"/>
      <stop offset="1" stop-color="var(--bee-dark)"/>
    </radialGradient>
    <clipPath id="emblem-clip">
      <circle cx="600" cy="768" r="153"/>
    </clipPath>
    <filter id="lift-shadow" x="-10%" y="-10%" width="120%" height="130%">
      <feDropShadow dx="2" dy="4" stdDeviation="3" flood-color="#7a4a00" flood-opacity="0.45"/>
    </filter>
  </defs>

  <path class="label-outline" d="
    M 599 38
    A 69 69 0 0 1 668 107
    L 668 553
    L 947 553
    Q 972 553 972 578
    L 972 937
    Q 972 962 947 962
    L 253 962
    Q 228 962 228 937
    L 228 578
    Q 228 553 253 553
    L 530 553
    L 530 107
    A 69 69 0 0 1 599 38 Z"/>

  <g class="emblem">
    <rect class="meadow" role="img" aria-label="Illustration of a wildflower meadow with clover, lavender and chamomile"
          x="440" y="790" width="320" height="135" fill="url(#meadow-tones)" clip-path="url(#emblem-clip)"/>
    <circle cx="600" cy="768" r="155" fill="none" stroke="url(#gold-ring)" stroke-width="5"/>
  </g>

  <path class="flight-trail" d="M 592 612 Q 625 628 640 605 Q 655 585 645 578"/>
  <ellipse class="bee" role="img" aria-label="Illustration of a flying honey bee"
           cx="556" cy="620" rx="36" ry="24" fill="url(#bee-tones)"/>

  <text class="product-name" x="600" y="776" text-anchor="middle" fill="url(#gold-letters)" filter="url(#lift-shadow)">Hunneg</text>
  <text class="tagline" x="478" y="700">e Maringer Glas</text>
  <text class="quantity" x="600" y="948" text-anchor="middle">500gr</text>

  <text class="producer-address" x="241" y="843">
    <tspan x="241" y="843">Jos Maringer, 14,</tspan>
    <tspan x="241" y="866">rue Pierre Faber,</tspan>
    <tspan x="241" y="889">L-7590 Miersch</tspan>
  </text>
  <text class="best-before" x="243" y="910">Am beschte virum:</text>

  <text class="storage-note" transform="translate(949 948) rotate(-90)" x="0" y="0">dréchen, kill andäischterstockéieren’</text>
</svg>
</body>
</html>
```